'Velomar' Nutritional supplements label design (UPDATED)

- 'Velomar' is a upscale health supplements brand
-The company will be packing the products in plastic bottles like other supplements
-Try to use a distinct design which is recognizable from distance
-Brand Logo is attached

-UPDATE- 2-

Label Dimensions and Design:

Hi Everyone,

Sorry for the late response caused by some very busy schedule.

Anyhow, here are the dimensions of the label (Self Adhesive) that we need:

Length of Label : 18cm
Height of Label : 6.5 cm

Product Names:

-Metabolism Formula
-Complete Multivitamins and Minerals (For Men, Women and Kids)
-Healthy Bones
-Skin Support
-Omega-3 oil for Healthy Heart

As for the ingredients just use Lorem Ipsum for now.

Many thanks to all of you in advance.

Target Market(s)

Middle Income families

Industry/Entity Type

Plastic

Requirements
Must have
• -Quality
-Effective
-Unique

```html
<!DOCTYPE html>
<html lang="en">
<head>
<meta charset="utf-8">
<title>Velomar Multi-Vitamins Label</title>
<link rel="stylesheet" href="https://fonts.googleapis.com/css2?family=Arimo:wght@400;700&family=Lilita+One&family=Montserrat:wght@500&family=Tinos:ital,wght@1,700&display=swap">
<style>
  :root {
    --yellow: #fdc400;
    --yellow-deep: #f7b200;
    --cream: #fff4b8;
    --teal: #1bc1c6;
    --navy: #1616a8;
    --orange: #f26a1f;
    --orange-dark: #d94e12;
    --red: #e3141d;
    --white: #ffffff;
  }
  * { margin: 0; padding: 0; box-sizing: border-box; }
  html, body { width: 1200px; height: 800px; overflow: hidden; }
  body {
    position: relative;
    background: linear-gradient(180deg, var(--yellow) 0%, var(--yellow-deep) 100%);
    font-family: "Arimo", Arial, sans-serif;
  }
  .layer { position: absolute; left: 0; top: 0; width: 1200px; height: 800px; }
  .brand {
    position: absolute; left: 190px; top: 258px;
    display: flex; align-items: center; gap: 26px;
  }
  .brand-dot { width: 120px; height: 120px; border-radius: 50%; background: var(--teal); }
  .brand-name {
    font-family: "Montserrat", Arial, sans-serif; font-weight: 500;
    font-size: 108px; line-height: 1; color: var(--teal); letter-spacing: 2px;
  }
  .tagline-strip {
    position: absolute; left: 330px; top: 370px; width: 560px; height: 40px;
    background: linear-gradient(90deg, rgba(255,238,120,0) 0%, rgba(255,238,120,.9) 15%, rgba(255,238,120,.9) 85%, rgba(255,238,120,0) 100%);
  }
  .tagline {
    position: absolute; left: 368px; top: 372px;
    display: flex; gap: 18px; font-weight: 700; font-size: 27px; color: var(--navy);
  }
  .tagline span::before { content: "•"; color: var(--orange); margin-right: 14px; }
  .product-title {
    position: absolute; left: 388px; top: 447px;
    font-family: "Lilita One", Arial, sans-serif; font-size: 56px; color: var(--red);
    -webkit-text-stroke: 7px var(--white); paint-order: stroke fill;
    transform: rotate(4deg); transform-origin: left center; letter-spacing: 1px;
  }
  .contents {
    position: absolute; left: 910px; top: 283px; width: 216px; height: 350px;
    text-align: center; padding-top: 30px;
  }
  .contents-main { color: var(--red); font-size: 21px; line-height: 30px; }
  .contents-extra { color: var(--navy); font-size: 16.5px; line-height: 24px; margin-top: 6px; }
  .claim {
    position: absolute; left: 58px; top: 664px; width: 520px; text-align: center;
    font-family: "Tinos", "Times New Roman", serif; font-style: italic; font-weight: 700;
    font-size: 27px; line-height: 37px; color: var(--white);
  }
</style>
</head>
<body>

<svg class="layer" viewBox="0 0 1200 800" aria-hidden="true">
  <path d="M0 48 C150 58 400 48 560 70 C650 82 660 170 710 190 C780 215 1000 200 1200 195" fill="none" stroke="#fff4b8" stroke-width="44"/>
  <path d="M0 578 C200 565 380 572 480 592 C560 608 600 675 680 684 C850 698 1050 684 1200 684" fill="none" stroke="#fff4b8" stroke-width="36"/>
</svg>

<svg class="layer" viewBox="0 0 1200 800" role="img" aria-label="Photograph of fresh vegetables and fruit: lettuce, broccoli, tomato, pineapple, bananas, pears, red pepper and radishes">
  <defs>
    <linearGradient id="produceTop" x1="0" x2="1" y1="0" y2="0">
      <stop offset="0" stop-color="#4f8a2a"/>
      <stop offset=".45" stop-color="#6a9a30"/>
      <stop offset=".6" stop-color="#d9a23c"/>
      <stop offset=".8" stop-color="#c8502a"/>
      <stop offset="1" stop-color="#d22a1e"/>
    </linearGradient>
  </defs>
  <path d="M0 0 H1200 V175 C1000 182 780 195 715 168 C665 148 650 68 560 52 C400 30 150 40 0 30 Z" fill="url(#produceTop)"/>
</svg>

<svg class="layer" viewBox="0 0 1200 800" role="img" aria-label="Photograph of fresh fruit and vegetables: red grapes, green grapes, orange, apples, carrots and spring onions">
  <defs>
    <linearGradient id="produceBottom" x1="0" x2="1" y1="0" y2="0">
      <stop offset="0" stop-color="#8e1420"/>
      <stop offset=".28" stop-color="#9ab545"/>
      <stop offset=".45" stop-color="#e3702c"/>
      <stop offset=".6" stop-color="#c93a2a"/>
      <stop offset=".75" stop-color="#e0782a"/>
      <stop offset="1" stop-color="#6fa83a"/>
    </linearGradient>
  </defs>
  <path d="M0 595 C200 582 380 590 480 610 C560 626 600 690 680 700 C850 714 1050 700 1200 700 V800 H0 Z" fill="url(#produceBottom)"/>
</svg>

<div class="brand">
  <div class="brand-dot"></div>
  <div class="brand-name">VELOMAR</div>
</div>

<div class="tagline-strip"></div>
<div class="tagline"><span>Quality</span><span>Effective</span><span>Unique</span></div>

<svg class="layer" viewBox="0 0 1200 800" aria-hidden="true">
  <path d="M345 448 C480 432 620 470 800 462 L820 492 L808 530 C640 545 500 500 372 500 L352 478 Z" fill="var(--orange)"/>
  <path d="M345 448 L352 478 L372 500 L360 470 Z" fill="var(--orange-dark)"/>
  <path d="M800 462 L820 492 L808 530 L812 495 Z" fill="var(--orange-dark)"/>
</svg>
<div class="product-title">Multi-Vitamins</div>

<svg class="layer" viewBox="0 0 1200 800" aria-hidden="true">
  <defs>
    <linearGradient id="panelFill" x1="0" x2="0" y1="0" y2="1">
      <stop offset="0" stop-color="#ffffff"/>
      <stop offset=".55" stop-color="#fff7a8"/>
      <stop offset="1" stop-color="#ffe600"/>
    </linearGradient>
  </defs>
  <path d="M924 283 H1112 A14 14 0 0 0 1126 297 V619 A14 14 0 0 0 1112 633 H924 A14 14 0 0 0 910 619 V297 A14 14 0 0 0 924 283 Z" fill="url(#panelFill)" stroke="var(--red)" stroke-width="3"/>
  <path d="M928 290 H1108 A12 12 0 0 0 1119 301 V615 A12 12 0 0 0 1108 626 H928 A12 12 0 0 0 917 615 V301 A12 12 0 0 0 928 290 Z" fill="none" stroke="var(--red)" stroke-width="1.5"/>
</svg>
<div class="contents">
  <div class="contents-main">VITAMINS<br>MINERALS<br>FRUITS &amp;<br>VEGETABLES</div>
  <div class="contents-extra">GREEN FOODS<br>ENZYMES<br>MUSHROOMS<br>AMINO ACIDS<br>ANTIOXIDANTS<br>LUTEIN<br>RESVERATROL</div>
</div>

<p class="claim">An all natural, 100% vegetarian<br>whole food multivitamin supplement</p>

</body>
</html>
```